Market place for used airplanes/helicopters/parts

http://www.vingtorget.se needs a facelift.

# What is it
Classifieds for used airplanes/helicopters/parts/spare parts/aviation literature, for people in Scandinavia. The number of classifieds is ~120-200. They are mainly in Swedish, English, Norwegian.

It's not a glamorous or luxurious business, but more for people with a genuine interest in flying, technical things.

Similar to sites like this, but they have much more classifieds than my site
http://www.skyquarry.com/list/list.aspx?ETID=1&setype=1&catid=6
http://www.lindqvistflyg.com/planes.asp?meny=1&typ=single
https://www.propwashdeals.com/cat.php?mode=listing&main=

# What I want
Design only - no code. I want a modern, maybe a bit bootstrap like, clean, simple, not flashy, web design. I want the design to be in English.

# Audience of the website
Aviation interested men, 45-65 years old, in the nordic countries (around Sweden).

# Logotype that could be used (but not necessarily)
http://www.vingtorget.se/flygplan_till_salu_large.jpg
http://www.vingtorget.se/flygplan_till_salu.eps

Reason: I decided to extend the deadline with 1 day. The reason is that I (unfortunately) managed to put the contest in the wrong category for 1 day + I want to give you all feedback (been too busy the whole day, sorry).

Hi all! 

Thanks everyone for the contributions you made. 

I will setup a poll for the designs that I like most. Will get back when I have more information. 

Thanks and have a nice weekend!
Kjell

Target Market(s)

45-65 old Scandinavian men

Industry/Entity Type

Business

Requirements
Must have
• - A list with classifieds on the first page, so the visitor easily can see new classifieds.
- A classifieds should be able to have more than one photo
- A simple navigation for showing classifieds from categories like airplanes, helicopters/gyrocopters, parts, literature, misc (maybe other categories) .... but still, it's just 100-200 ads so it's not needed that much filtration.

- A placeholder/way of showing aviation news/clips. In the old design I had, it was a column to the right. It's enough to show maybe 2-5 placeholders.
- A placeholder for PlaceAds ads somewhere on the site.
Should not have
• - Carousels
- Too much clutter

```html
<!DOCTYPE html>
<html lang="en">
<head>
<meta charset="utf-8">
<title>Vingtorget – Aircraft classifieds</title>
<link rel="stylesheet" href="https://fonts.googleapis.com/css2?family=Arimo:wght@400;700&display=swap">
<style>
  :root {
    --accent: #00a8e2;
    --accent-soft: #22bdf0;
    --header-bg: #ececec;
    --page-bg: #f1f1f1;
    --nav-bg: #2b2b2b;
    --row-bg: #e2e2e2;
    --row-open: #d6d6d6;
    --row-text: #9a9a9a;
    --row-text-open: #555;
    --body-text: #444;
    --footer-bg: #ffffff;
    --ad-bg: #1b1b1b;
    --ad-text: #f2cf7c;
    --brand: #1d6fb3;
  }
  * { box-sizing: border-box; margin: 0; padding: 0; }
  html, body { width: 1200px; height: 900px; overflow: hidden; }
  body {
    font-family: "Arimo", Arial, sans-serif;
    background: var(--page-bg);
    color: var(--body-text);
    position: relative;
  }
  .top-stripe { height: 4px; background: var(--accent); }
  .site-header {
    height: 124px;
    background: var(--header-bg);
    border-bottom: 2px solid #fff;
    position: relative;
  }
  .brand {
    position: absolute; left: 136px; top: 58px;
    display: flex; align-items: center; gap: 10px;
    font-size: 36px; font-weight: 700; color: var(--brand); letter-spacing: 1px;
  }
  .brand-mark { width: 22px; height: 22px; background: var(--accent); }
  .publish-btn {
    position: absolute; left: 924px; top: 17px;
    width: 139px; height: 36px; border-radius: 6px;
    background: linear-gradient(var(--accent-soft), var(--accent));
    color: #fff; font-size: 13px;
    display: flex; align-items: center; padding-left: 7px; gap: 6px;
  }
  .publish-btn svg { flex: none; }
  .main-nav {
    position: absolute; left: 643px; top: 67px;
    width: 420px; height: 36px; border-radius: 6px;
    background: var(--nav-bg);
    display: flex; align-items: center; gap: 36px;
    padding-left: 18px;
  }
  .main-nav a { color: #fff; font-size: 13px; text-decoration: none; }

  .listings { position: absolute; left: 135px; top: 147px; width: 660px; }
  .listing-row {
    height: 34px; margin-bottom: 2px; border-radius: 3px;
    background: var(--row-bg);
    display: flex; align-items: center;
    font-size: 13px; font-weight: 700; color: var(--row-text);
  }
  .listing-row .toggle { width: 40px; text-align: center; font-size: 20px; font-weight: 400; color: #9a9a9a; }
  .listing-row.is-open { background: var(--row-open); color: var(--row-text-open); }
  .listing-row.is-open .toggle { color: #777; }
  .listing-detail {
    position: relative; height: 202px; padding: 8px 0 0 8px;
    font-size: 11.3px; line-height: 18.4px; color: var(--body-text);
  }
  .listing-detail p { width: 418px; }
  .listing-photo {
    position: absolute; left: 435px; top: 8px; width: 216px; height: 144px;
    border: 1px solid #b9b9b9;
    background: linear-gradient(160deg, #8a8f96 0%, #a09a93 45%, #7e7566 100%);
  }

  .sidebar { position: absolute; left: 808px; top: 147px; width: 255px; }
  .news-clip {
    height: 197px; background: #111; position: relative; overflow: hidden;
  }
  .clip-title { position: absolute; top: 3px; left: 6px; right: 6px; display: flex; justify-content: space-between; font-size: 7px; color: #ddd; }
  .clip-frame {
    position: absolute; top: 20px; left: 0; right: 0; height: 142px;
    background: linear-gradient(180deg, #9fb3c2 0%, #6e8a62 40%, #5f7a6a 70%, #4d6570 100%);
  }
  .clip-play { position: absolute; left: 110px; top: 77px; }
  .clip-controls { position: absolute; bottom: 0; left: 0; right: 0; height: 16px; background: #222; border-top: 1px solid #444; }
  .ad-slot {
    margin-top: 10px; height: 227px; background: var(--ad-bg);
    display: flex; align-items: center; justify-content: center; text-align: center;
    color: var(--ad-text); font-size: 27px; line-height: 40px;
  }

  .site-footer {
    position: absolute; left: 0; top: 800px; width: 1200px; height: 100px;
    background: var(--footer-bg); border-top: 1px solid #cfcfcf; text-align: center;
  }
  .footer-nav { margin-top: 25px; font-size: 11.5px; color: #555; }
  .footer-nav span { margin: 0 9px; }
  .copyright { margin-top: 28px; font-size: 9.5px; color: #555; }
</style>
</head>
<body>
  <div class="top-stripe"></div>
  <header class="site-header">
    <div class="brand"><span class="brand-mark"></span>VINGTORGET</div>
    <div class="publish-btn">
      <svg width="24" height="24" viewBox="0 0 24 24"><rect x="1.5" y="1.5" width="21" height="21" rx="3" fill="#fff" stroke="#333" stroke-width="2"/><path d="M6 12l4 4 8-9" fill="none" stroke="#333" stroke-width="2.5"/></svg>
      Publish your ad
    </div>
    <nav class="main-nav">
      <a href="#">Airplanes</a><a href="#">Helicopters</a><a href="#">Parts</a><a href="#">Literature</a><a href="#">Misc</a>
    </nav>
  </header>

  <main class="listings">
    <div class="listing-row"><span class="toggle">+</span>Vacuumpump</div>
    <div class="listing-row"><span class="toggle">+</span>Dynavia DX-220</div>
    <div class="listing-row is-open"><span class="toggle">−</span>Aerobatic Ranger R-7C LN-SKX</div>
    <div class="listing-detail">
      <p>Experimental clipped wing +9/-6G airshow performer for sale in Norway. Two stroke Bluecap B560 fully inverted systems. Built in 1994, new wings in 2011. Total time 401 hours, engine 135 hours. Customized pocket fighter with short legs and great aerobatic performance for 80 kg pilot. Noise cancelling intercom, new radios and avionics. Transponder mode C, ELT, BRS repacked 2012. Newly re-certified by Fjordvinge AS.<br>
      Asking 26.000 EUR<br>
      Namn: Arvid Holmstrand, E-posta<br>
      Telefon: +4790123456<br>
      Datum: 2013-10-04 12:23:08</p>
      <div class="listing-photo" role="img" aria-label="Photo of the red and white aerobatic plane in flight over farmland"></div>
    </div>
    <div class="listing-row"><span class="toggle">+</span>LN-MPX FT204K 1973 til salgs!</div>
    <div class="listing-row"><span class="toggle">+</span>Mauler K4 -82/89</div>
    <div class="listing-row"><span class="toggle">+</span>HANGARPLATS LEDIG I FALKÖPING.</div>
    <div class="listing-row"><span class="toggle">+</span>Vacuumpump</div>
    <div class="listing-row"><span class="toggle">+</span>Dynavia DX-220</div>
    <div class="listing-row"><span class="toggle">+</span>Aerobatic Ranger R-7C LN-SKX</div>
    <div class="listing-row"><span class="toggle">+</span>LN-MPX FT204K 1973 til salgs!</div>
    <div class="listing-row"><span class="toggle">+</span>Mauler K4 -82/89</div>
    <div class="listing-row"><span class="toggle">+</span>HANGARPLATS LEDIG I FALKÖPING.</div>
  </main>

  <aside class="sidebar">
    <div class="news-clip">
      <div class="clip-title"><span>Float plane clip</span><span>Share &nbsp; More info</span></div>
      <div class="clip-frame" role="img" aria-label="Video still of a float plane on a river beneath a bridge"></div>
      <svg class="clip-play" width="36" height="26" viewBox="0 0 36 26"><rect width="36" height="26" rx="5" fill="#1a1a1a" opacity="0.85"/><path d="M14 7l10 6-10 6z" fill="#fff"/></svg>
      <div class="clip-controls"></div>
    </div>
    <div class="ad-slot">PlaceAds ads<br>Here</div>
  </aside>

  <footer class="site-footer">
    <div class="footer-nav">Airplanes<span>|</span>Helicopters<span>|</span>Parts<span>|</span>Literature<span>|</span>Misc</div>
    <div class="copyright">© 2013 http://www.vingtorget.se All Rights Reserved.</div>
  </footer>
</body>
</html>
```